Redesign of Quietude Orchard website

- I would like to redesign my ministry website (velno.org)
- Re-brand it with my new logo.

I am looking for something professional and artistic, and focused on creating a good user experience.

The purpose of the site is to:
- Expose TOVKA to the world
- Inform the public about what we are all about.
- Promote my publications (https://www.bookvendra.example/Final-Pilgrim-Leaving-Patterned-Realm-ebook/dp/Q47TX2WK9R/ref=dp_kinw_strp_1)

I don't have to many media material, so I am open to suggestions if the provided images will enhance the look and feel of the site.

Target Market(s)

All English speaking christians , and aspiring Christians around the world.

Industry/Entity Type

Religious

Number of Pages Required

3 page

Font styles to use
Sans Serif

Requirements
Must have
• - Add donation link through CoinDrift
• - A mission page that contains the description found on the "About us" page on Velno.org
• - A personal author page that will include my bio, publication, and contact information. People should be able to email me right from the page
• - Social media links
Nice to have
• - An address book, were people can send us their contact information.

```html
<!DOCTYPE html>
<html lang="en">
<head>
<meta charset="utf-8">
<title>TOVKA – A Voice to All Nations</title>
<link rel="stylesheet" href="https://fonts.googleapis.com/css2?family=Cinzel:wght@400;700&family=Open+Sans:wght@400;600;700&display=swap">
<style>
:root{
  --navy:#0d3a63;
  --navy-deep:#062a4c;
  --blue-band:#0a4a7e;
  --gold:#e0960c;
  --gold-light:#f0c23a;
  --text:#555;
  --text-dark:#333;
  --light-bg:#f6f6f6;
  --footer-bg:#e6e6e6;
  --white:#fff;
}
*{margin:0;padding:0;box-sizing:border-box}
html,body{width:1200px;height:2311px;overflow:hidden;background:var(--white)}
body{font-family:"Open Sans",sans-serif;color:var(--text);position:relative}

/* header */
.site-header{position:absolute;left:0;top:0;width:1200px;height:131px;background:var(--white)}
.brand{position:absolute;left:74px;top:50px;display:flex;align-items:center;gap:10px}
.brand-mark{width:14px;height:14px;background:var(--gold);border-radius:50%}
.brand-name{font-family:"Open Sans",sans-serif;font-size:40px;font-weight:700;color:var(--navy);line-height:1}
.donate-btn{position:absolute;left:885px;top:20px;width:241px;height:47px;border-radius:24px;background:linear-gradient(#fcd56a,#f2a51a);border:1px solid #d98d0a;display:flex;align-items:center;justify-content:center;font-weight:700;font-size:17px;color:var(--navy)}
.main-nav{position:absolute;right:74px;top:91px;display:flex;gap:44px}
.main-nav a{font-family:"Cinzel",serif;font-size:15px;color:var(--text-dark);text-decoration:none;letter-spacing:.5px;padding-bottom:8px}
.main-nav a.active{color:var(--navy);font-weight:700;border-bottom:3px solid var(--navy)}

/* hero */
.hero{position:absolute;left:0;top:131px;width:1200px;height:508px;background:radial-gradient(circle at 25% 15%,#f4d56a 0,#b7b53a 18%,#6f8f2c 45%,#3f5a1f 80%,#2b3a17 100%)}
.hero-title{position:absolute;left:74px;top:170px;font-family:"Cinzel",serif;font-size:66px;color:var(--white);line-height:1}
.hero-sub{position:absolute;left:74px;top:250px;font-weight:700;font-size:46px;color:var(--white)}
.hero-dots{position:absolute;left:74px;top:443px;display:flex;gap:7px}
.hero-dots span{width:10px;height:10px;border-radius:50%;background:var(--white)}
.hero-dots span:first-child{background:var(--gold-light)}
.quick-contact{position:absolute;left:793px;top:60px;width:333px;height:391px;background:var(--white);box-shadow:0 2px 8px rgba(0,0,0,.25)}
.quick-contact h2{height:64px;background:var(--navy);color:var(--white);font-family:"Cinzel",serif;font-size:31px;font-weight:400;display:flex;align-items:center;justify-content:center}
.qc-field{position:absolute;left:21px;width:292px;height:41px;border:1px solid #ccc;border-radius:2px;font-size:13px;color:#666;padding:10px 12px}
.qc-submit{position:absolute;left:21px;top:320px;width:292px;height:50px;background:linear-gradient(#f2a81e,#d98a06);color:var(--white);font-family:"Cinzel",serif;font-size:23px;display:flex;align-items:center;justify-content:center;letter-spacing:1px}

/* buttons and titles */
.btn{position:absolute;background:var(--gold);color:var(--white);font-family:"Cinzel",serif;font-size:18px;display:flex;align-items:center;justify-content:center;letter-spacing:.5px}
.section-title{font-family:"Cinzel",serif;font-weight:700;color:var(--navy);letter-spacing:1.5px}

/* mission */
.mission-title{position:absolute;left:0;top:690px;width:1200px;text-align:center;font-size:34px}
.mission-text{position:absolute;left:78px;top:746px;width:1048px;text-align:center;font-size:15px;line-height:26px}

/* bio */
.bio{position:absolute;left:0;top:981px;width:1200px;height:453px;background:var(--light-bg)}
.bio-title{position:absolute;left:80px;top:42px;font-size:33px}
.bio-text{position:absolute;left:74px;top:99px;width:690px;font-size:15.5px;line-height:29px}
.bio-text p+p{margin-top:3px}
.bio-list{list-style:none;margin-top:2px}
.bio-list li{display:flex;align-items:center;gap:8px;font-weight:600;color:var(--text-dark);font-size:15px;line-height:34px}
.bio-photo{position:absolute;left:793px;top:49px;width:333px;height:349px;background:var(--white);border:1px solid #ccc;padding:6px}
.bio-photo div{width:100%;height:100%;background:linear-gradient(135deg,#cbb9c0,#e8e0dc 45%,#7a8fb5)}

/* publications */
.pubs{position:absolute;left:0;top:1434px;width:1200px;height:408px}
.pubs-left{position:absolute;left:0;top:0;width:765px;height:408px;background:radial-gradient(circle at 18% 45%,#1a5f95 0,#0b3e6b 45%,var(--navy-deep) 100%)}
.pubs-right{position:absolute;left:765px;top:0;width:435px;height:408px;background:var(--blue-band)}
.book-cover{position:absolute;left:74px;top:60px;width:199px;height:311px;background:linear-gradient(90deg,#e8d640 0,#e8d640 8%,#6d5a3e 8%,#4a4a4a 60%,#2c2c2c)}
.pubs-title{position:absolute;left:317px;top:50px;font-family:"Cinzel",serif;font-size:33px;color:var(--white);letter-spacing:1px}
.pub-name{position:absolute;left:317px;top:103px;font-weight:700;font-size:20px;color:var(--gold-light)}
.pub-sub{position:absolute;left:317px;top:131px;font-size:19px;color:var(--white)}
.pub-author{position:absolute;left:317px;top:164px;font-weight:600;font-size:14px;color:var(--gold)}
.pub-text{position:absolute;left:317px;top:192px;width:420px;font-size:15px;line-height:26px;color:var(--white)}
.service-card{position:absolute;left:28px;width:333px;border:1px solid #3f7cb6;background:linear-gradient(#0a4a82,#083b69);display:flex;align-items:center}
.service-card svg{margin-left:30px;flex:none}
.service-card span{margin-left:40px;font-family:"Cinzel",serif;font-weight:700;font-size:32px;line-height:30px;color:var(--gold-light)}

/* newsletter */
.news-title{position:absolute;left:0;top:1872px;width:1200px;text-align:center;font-size:34px}
.news-text{position:absolute;left:0;top:1930px;width:1200px;text-align:center;font-size:15px}
.news-form{position:absolute;left:343px;top:1973px;width:512px;height:46px;border:1px solid #ccc;display:flex;align-items:center}
.news-form .ph{flex:1;display:flex;align-items:center;gap:12px;padding-left:14px;font-size:14px;color:#999}
.news-form .go{width:62px;height:46px;margin-right:-1px;background:var(--gold);display:flex;align-items:center;justify-content:center}

/* footer */
.site-footer{position:absolute;left:0;top:2059px;width:1200px;height:252px;background:var(--footer-bg)}
.foot-brand{position:absolute;left:74px;top:68px;display:flex;align-items:center;gap:8px}
.foot-brand .brand-name{font-size:30px}
.foot-copy{position:absolute;left:74px;top:120px;font-size:14px;line-height:23px;color:#666}
.social{position:absolute;left:74px;top:193px;display:flex;gap:15px}
.social span{width:22px;height:22px;background:var(--navy);border-radius:3px}
.foot-head{position:absolute;top:30px;font-weight:700;font-size:15px;color:var(--navy)}
.foot-links{position:absolute;top:62px;font-size:13.5px;line-height:32px;color:var(--text-dark);list-style:none}
.foot-contact{position:absolute;left:705px;top:63px;font-size:13.5px;line-height:21px;color:var(--text-dark)}
.foot-contact b{color:var(--gold);font-weight:600}
</style>
</head>
<body>

<header class="site-header">
  <div class="brand"><span class="brand-mark"></span><span class="brand-name">TOVKA</span></div>
  <div class="donate-btn">Donate with CoinDrift</div>
  <nav class="main-nav">
    <a class="active" href="#">Home</a><a href="#">About us</a><a href="#">Mission</a><a href="#">Author</a><a href="#">Publications</a><a href="#">Donation</a><a href="#">Contact us</a>
  </nav>
</header>

<section class="hero" role="img" aria-label="Sunlit orchard with blossoming trees">
  <div class="hero-title">TOVKA</div>
  <div class="hero-sub">A Voice to All Nation</div>
  <div class="hero-dots"><span></span><span></span><span></span><span></span></div>
  <form class="quick-contact">
    <h2>QUICK CONTACT</h2>
    <div class="qc-field" style="top:81px">Name</div>
    <div class="qc-field" style="top:129px">Email Address</div>
    <div class="qc-field" style="top:176px">Phone No.</div>
    <div class="qc-field" style="top:225px;height:89px">Message</div>
    <div class="qc-submit">SUBMIT</div>
  </form>
</section>

<section>
  <h2 class="section-title mission-title">MISSION STATEMENT</h2>
  <p class="mission-text">Quietude Orchard is a gathering of believers which has for purpose to seek the face of God for an authentic restoration of the church as a body of born again believers around the world. In this age of great scientific innovations and discoveries, the world is undergoing a transformation that only those who can look at it from outside can discern in what direction the change is taking us. Our mindset is being reshaped by the media and new ideas that are inclined toward vices rather than values.</p>
  <div class="btn" style="left:517px;top:883px;width:165px;height:47px">Read More</div>
</section>

<section class="bio">
  <h2 class="section-title bio-title">BIOGRAPHY</h2>
  <div class="bio-text">
    <p>Elias Morven is a Bible teacher and missionary of the Gospel of Jesus Christ. He is the president and founder of TOVKA, a missionary organization dedicated to preparing believers for the return of the Lord Jesus Christ. He holds a Bachelor's degree in Computer Science from the University of Northern Calder and has been in ministry for over 15 years.</p>
    <p>Elias hopes to show to his generation that:</p>
    <ul class="bio-list">
      <li><svg width="14" height="14" viewBox="0 0 14 14"><circle cx="7" cy="7" r="7" fill="#0d3a63"/><path d="M3.8 7.2l2.2 2.2 4.2-4.4" stroke="#fff" stroke-width="1.8" fill="none"/></svg>Faith and science are not mutually exclusive as many are lead to believe.</li>
      <li><svg width="14" height="14" viewBox="0 0 14 14"><circle cx="7" cy="7" r="7" fill="#0d3a63"/><path d="M3.8 7.2l2.2 2.2 4.2-4.4" stroke="#fff" stroke-width="1.8" fill="none"/></svg>The Holy Spirit is still working today as He did back 2000 years ago.</li>
    </ul>
  </div>
  <div class="btn" style="left:74px;top:350px;width:166px;height:48px">Read More</div>
  <div class="bio-photo"><div role="img" aria-label="Portrait photo of the author and his wife"></div></div>
</section>

<section class="pubs">
  <div class="pubs-left">
    <div class="book-cover" role="img" aria-label="Book cover of The Final Pilgrim"></div>
    <h2 class="pubs-title">My Publications</h2>
    <div class="pub-name">The Final Pilgrim:</div>
    <div class="pub-sub">Leaving a Patterned Realm</div>
    <div class="pub-author">By Elias Brandt Morven</div>
    <p class="pub-text">Society has changed faster in the past hundred years than in any other period of human history. This change has profound spiritual implications that most of us are completely unaware of.</p>
    <div class="btn" style="left:316px;top:314px;width:164px;height:48px">Read More</div>
  </div>
  <div class="pubs-right">
    <div class="service-card" style="top:52px;height:91px">
      <svg width="50" height="50" viewBox="0 0 50 50" fill="none" stroke="#fff" stroke-width="3"><rect x="4" y="8" width="42" height="38" rx="2"/><line x1="4" y1="18" x2="46" y2="18"/><line x1="14" y1="3" x2="14" y2="12"/><line x1="36" y1="3" x2="36" y2="12"/><g fill="#fff" stroke="none"><rect x="10" y="23" width="6" height="6"/><rect x="22" y="23" width="6" height="6"/><rect x="34" y="23" width="6" height="6"/><rect x="10" y="34" width="6" height="6"/><rect x="22" y="34" width="6" height="6"/><rect x="34" y="34" width="6" height="6"/></g></svg>
      <span>SUNDAY<br>SERVICES</span>
    </div>
    <div class="service-card" style="top:162px;height:90px">
      <svg width="50" height="50" viewBox="0 0 50 50" fill="none" stroke="#fff" stroke-width="3" stroke-linejoin="round"><path d="M25 44V14l-6-9-5 14-8 12 8 13z"/><path d="M25 44V14l6-9 5 14 8 12-8 13z"/></svg>
      <span>PRAYER</span>
    </div>
    <div class="service-card" style="top:269px;height:93px">
      <svg width="54" height="50" viewBox="0 0 54 50" fill="#fff"><circle cx="27" cy="8" r="6"/><rect x="17" y="17" width="20" height="6" rx="2"/><circle cx="12" cy="31" r="5"/><circle cx="27" cy="31" r="5"/><circle cx="42" cy="31" r="5"/><path d="M3 48c0-8 4-11 9-11s9 3 9 11zM18 48c0-8 4-11 9-11s9 3 9 11zM33 48c0-8 4-11 9-11s9 3 9 11z"/></svg>
      <span>PROPHETIC<br>SEASON</span>
    </div>
  </div>
</section>

<section>
  <h2 class="section-title news-title">Newsletter Sign Up</h2>
  <p class="news-text">Vestibulum ante ipsum primis in faucibus orci luctus et ultrices posuere cubilia</p>
  <form class="news-form">
    <div class="ph"><svg width="20" height="15" viewBox="0 0 20 15" fill="none" stroke="#bbb" stroke-width="1.5"><rect x="1" y="1" width="18" height="13"/><path d="M1 1l9 7 9-7"/></svg>Enter Email Address</div>
    <div class="go"><svg width="14" height="20" viewBox="0 0 14 20"><path d="M3 3l7 7-7 7" stroke="#fff" stroke-width="3.5" fill="none"/></svg></div>
  </form>
</section>

<footer class="site-footer">
  <div class="foot-brand"><span class="brand-mark"></span><span class="brand-name">TOVKA</span></div>
  <p class="foot-copy">Copyright © 2016. All Right Reserved<br>Privacy Policy</p>
  <div class="social"><span></span><span></span><span></span><span></span><span></span><span></span></div>
  <div class="foot-head" style="left:434px">SITE MAP</div>
  <ul class="foot-links" style="left:434px"><li>Home</li><li>About us</li><li>Mission</li><li>Author</li></ul>
  <ul class="foot-links" style="left:533px"><li>Publications</li><li>Donation</li><li>Contact us</li></ul>
  <div class="foot-head" style="left:705px">CONTACT INFORMATION</div>
  <p class="foot-contact"><b>Mailing Address:</b><br>QUIETUDE ORCHARD<br>42 Alder Lane<br>Brookfield, Maine 04999<br>USA</p>
</footer>

</body>
</html>
```